Brightvault Banner Ad Campaign

Overview
We require 3 different banners within the same brief, but would like you to just produce 1 banner for your initial bid.

We require a punchy message to be delivered to existing poker players. We offer the opportunity for players to play poker with our money (ie. ‘staked’), sharing the profits if they win, us taking the losses if they lose. 'Sharks' is a poker term for skilled winning players who eat up the 'fish'.. term for unskilled losing players.

The players we stake are playing no risk poker and enjoy the support of our team, as well as professional coaching free of charge. Our key messages are bulleted below, some suggestions for tag lines also. We would like some creativity input in the design/ tag lines plus of course the banners themselves delivered. See www.brightvault-example.com for our colour scheme and shark fin logo and to get a feel for what we do.

3 different pieces of artwork required:-
2 'square', sized – 180x150
1 'normal' banner sized
Clearly we may want to resize these slightly for different uses.

Some messages we want to convey:-
• Free Bankroll $$$$
• Free Pro Coaching
• Part of a team & support network
• Risk free, stress free poker
• We are the best staking operation

Possible tag lines:-
Losing your bite?
Sharpen your teeth!
Get staked today!
Join the best, crush the rest

Thanks
Dorian
Updates

Guys,

we have a strong theme with the Shark and/or our red fin logo, can you focus on that in your designs please. a Shark as per brief is a successful poker player .. a 'fish' is what they prey on..

Thanks

Dorian

```html
<!DOCTYPE html>
<html lang="en">
<head>
<meta charset="utf-8">
<title>Brightvault Banner</title>
<link rel="stylesheet" href="https://fonts.googleapis.com/css2?family=Roboto+Condensed:wght@700&family=Roboto:wght@700&display=swap">
<style>
  :root {
    --backdrop: #b99a74;
    --banner-black: #000000;
    --brand-red: #e1232b;
    --text-white: #ffffff;
    --card-light: #ffffff;
    --card-shade: #cfcfcf;
    --chip-tone: #a3151b;
    --chip-dark: #2a0a0b;
    --hook-grey: #bdbdbd;
  }
  * { margin: 0; padding: 0; box-sizing: border-box; }
  html, body {
    width: 1200px;
    height: 927px;
    overflow: hidden;
    background: var(--backdrop);
  }
  .canvas {
    position: relative;
    width: 1200px;
    height: 927px;
    background: var(--backdrop);
  }
  .banner {
    position: absolute;
    left: 49px;
    top: 91px;
    width: 1104px;
    height: 135px;
    background: var(--banner-black);
    overflow: hidden;
  }
  .brand-mark {
    position: absolute;
    left: 46px;
    top: 21px;
    width: 94px;
    height: 94px;
    border-radius: 50%;
    background: var(--brand-red);
  }
  .brand-name {
    position: absolute;
    left: 166px;
    top: 10px;
    font-family: "Roboto", Arial, sans-serif;
    font-weight: 700;
    font-size: 50px;
    line-height: 1;
    letter-spacing: -0.5px;
    color: var(--brand-red);
  }
  .brand-claim {
    position: absolute;
    left: 331px;
    top: 65px;
    font-family: "Roboto Condensed", Arial, sans-serif;
    font-weight: 700;
    font-size: 15px;
    letter-spacing: 0.4px;
    color: var(--text-white);
  }
  .brand-tagline {
    position: absolute;
    left: 170px;
    top: 83px;
    font-family: "Roboto Condensed", Arial, sans-serif;
    font-weight: 700;
    font-size: 28px;
    line-height: 1.2;
    letter-spacing: 0.8px;
    color: var(--text-white);
  }
  .card-fan {
    position: absolute;
    left: 500px;
    top: 5px;
    width: 146px;
    height: 128px;
  }
  .benefits {
    position: absolute;
    left: 649px;
    top: 25px;
    list-style: none;
    font-family: "Roboto Condensed", Arial, sans-serif;
    font-weight: 700;
    font-size: 20px;
    line-height: 26px;
    letter-spacing: 0.7px;
    color: var(--text-white);
  }
  .benefits li::before {
    content: "\2022\00a0";
  }
  .benefits .sep::before {
    content: "\00a0\2022\00a0";
  }
  .catch-line {
    position: absolute;
    left: 954px;
    top: 3px;
    font-family: "Roboto Condensed", Arial, sans-serif;
    font-weight: 700;
    font-size: 17px;
    letter-spacing: 0.5px;
    color: var(--text-white);
  }
  .hook-icon {
    position: absolute;
    left: 1084px;
    top: 0;
    width: 18px;
    height: 34px;
  }
  .chip-stack {
    position: absolute;
    left: 998px;
    top: 50px;
    width: 76px;
    height: 72px;
    border-radius: 42% 42% 46% 46%;
    background: radial-gradient(ellipse at 50% 40%, var(--chip-tone), var(--chip-dark) 80%);
  }
</style>
</head>
<body>
  <main class="canvas">
    <section class="banner" aria-label="Brightvault staking banner">
      <div class="brand-mark" aria-hidden="true"></div>
      <div class="brand-name">Brightvault</div>
      <div class="brand-claim">Best staking operation</div>
      <div class="brand-tagline">Bring out the shark in you</div>

      <svg class="card-fan" viewBox="0 0 146 128" role="img" aria-label="Fanned playing cards from ten down to ace">
        <defs>
          <linearGradient id="card-fill" x1="0" y1="0" x2="1" y2="1">
            <stop offset="0" stop-color="var(--card-shade)"/>
            <stop offset="0.55" stop-color="var(--card-light)"/>
            <stop offset="1" stop-color="var(--card-shade)"/>
          </linearGradient>
        </defs>
        <path d="M4 12 Q4 8 8 7 L66 2 Q70 2 72 5 L142 58 Q144 60 144 63 L144 122 Q144 126 140 126 L98 126 Q95 126 93 124 L6 58 Q4 56 4 53 Z" fill="url(#card-fill)"/>
      </svg>

      <ul class="benefits">
        <li>Be Part of our Team!<span class="sep">Free Bankroll</span></li>
        <li>Free Pro Coaching &amp; Network Support</li>
        <li>No Risk Poker</li>
      </ul>

      <div class="catch-line">Catch that fish!</div>
      <svg class="hook-icon" viewBox="0 0 18 34" aria-hidden="true">
        <circle cx="12" cy="3" r="2" fill="none" stroke="var(--hook-grey)" stroke-width="1.4"/>
        <path d="M12 5 V24 a5 5 0 0 1 -10 0 V19 l3 4" fill="none" stroke="var(--hook-grey)" stroke-width="1.6"/>
      </svg>

      <div class="chip-stack" role="img" aria-label="Stacked red poker chips"></div>
    </section>
  </main>
</body>
</html>
```